Business Card for boutique psychology business

Business card for boutique psychology practice in Melbourne. I want them to be relatively simply with the logo and backing colour taking up the front side. Then, text on the back, with my name; professional title (Clinical Psychologist); website - mirotherapy.com.au; email: hello@mirotherapy.com.au; insta: @mirotherapy.studio
Back should also have the words: Listen. Restore. Grow
Fonts used for logo are: Mikea Demo and Gotham Medium. Use something for back text that will compliment these.
Brand colours uploaded below. I'd like to see options in both olive and blush.

```html
<!DOCTYPE html>
<html lang="en">
<head>
<meta charset="utf-8">
<title>Miro Therapy – Business Cards</title>
<link rel="stylesheet" href="https://fonts.googleapis.com/css2?family=Cormorant+Garamond:wght@300&family=Montserrat:wght@400;500&display=swap">
<style>
  :root {
    --backdrop: #d4d9d9;
    --card: #efefec;
    --olive: #474c2a;
    --ink: #3a3a36;
    --rule: #5a5e40;
  }
  * { margin: 0; padding: 0; box-sizing: border-box; }
  html, body { width: 1200px; height: 881px; overflow: hidden; }
  body {
    background: var(--backdrop);
    position: relative;
    font-family: "Montserrat", sans-serif;
  }
  .card {
    position: absolute;
    width: 520px;
    height: 298px;
    background: var(--card);
    box-shadow: 0 14px 30px rgba(60, 70, 70, 0.18);
  }
  .card-front { left: 620px; top: 150px; }
  .card-back  { left: 60px;  top: 430px; }

  .wordmark {
    color: var(--olive);
    font-family: "Montserrat", sans-serif;
    font-weight: 500;
    line-height: 1;
    letter-spacing: 0.01em;
  }
  .card-front .wordmark {
    position: absolute;
    left: 0; right: 0; top: 50%;
    transform: translateY(-50%);
    text-align: center;
    font-size: 64px;
  }

  .back-logo {
    position: absolute;
    left: 28px; top: 0; bottom: 70px;
    width: 200px;
    display: flex;
    align-items: center;
    justify-content: center;
  }
  .back-logo .wordmark { font-size: 34px; text-align: center; }

  .divider {
    position: absolute;
    left: 248px; top: 40px;
    width: 1px; height: 168px;
    background: var(--rule);
  }

  .details {
    position: absolute;
    left: 268px; top: 42px;
    color: var(--ink);
  }
  .details .name {
    font-family: "Cormorant Garamond", serif;
    font-weight: 300;
    font-size: 28px;
    line-height: 1;
    color: var(--olive);
  }
  .details .title {
    font-size: 12.5px;
    margin-top: 6px;
    margin-bottom: 26px;
  }
  .contact { list-style: none; }
  .contact li {
    display: flex;
    align-items: center;
    gap: 8px;
    font-size: 12.5px;
    line-height: 1;
    margin-bottom: 10px;
    white-space: nowrap;
  }
  .contact svg { width: 11px; height: 11px; flex: none; }

  .tagline {
    position: absolute;
    left: 0; right: 0; bottom: 34px;
    text-align: center;
    font-size: 13px;
    color: var(--ink);
    letter-spacing: 0.02em;
  }
</style>
</head>
<body>
  <section class="card card-front" aria-label="Card front">
    <div class="wordmark">miro therapy</div>
  </section>

  <section class="card card-back" aria-label="Card back">
    <div class="back-logo"><div class="wordmark">miro therapy</div></div>
    <div class="divider"></div>
    <div class="details">
      <div class="name">Miro</div>
      <div class="title">Clinical Psychologist</div>
      <ul class="contact">
        <li>
          <svg viewBox="0 0 12 12" aria-hidden="true"><circle cx="6" cy="6" r="5" fill="none" stroke="#474c2a" stroke-width="1.2"/><ellipse cx="6" cy="6" rx="2.2" ry="5" fill="none" stroke="#474c2a" stroke-width="1"/><line x1="1" y1="6" x2="11" y2="6" stroke="#474c2a" stroke-width="1"/></svg>
          mirotherapy.com.au
        </li>
        <li>
          <svg viewBox="0 0 12 12" aria-hidden="true"><rect x="0.5" y="2.5" width="11" height="7" fill="#474c2a"/><polyline points="0.5,2.5 6,7 11.5,2.5" fill="none" stroke="#efefec" stroke-width="1"/></svg>
          hello@mirotherapy.com.au
        </li>
        <li>
          <svg viewBox="0 0 12 12" aria-hidden="true"><rect x="1.5" y="1.5" width="9" height="9" fill="none" stroke="#474c2a" stroke-width="1.2"/></svg>
          @mirotherapy.studio
        </li>
      </ul>
    </div>
    <div class="tagline">Listen. Restore. Grow</div>
  </section>
</body>
</html>
```